Need updated stationery design for chiropractic clinic

We recently moved our office and are looking to refresh our letterhead, business cards, presentation folder and envelopes. I tend to prefer simple, clean designs. We communicate with a lot of attorneys and want to exude professionalism. I have attached our logo and 2 additional versions (all white and white letters instead of grey).

Target Market(s)

Other medical professionals and attorneys. Business cards will go to patients as well.

Industry/Entity Type

Healthcare

```html
<!DOCTYPE html>
<html lang="en">
<head>
<meta charset="utf-8">
<title>SpineWell Injury Care Clinic – Business Card</title>
<link rel="stylesheet" href="https://fonts.googleapis.com/css2?family=Roboto:wght@400;700&family=Roboto+Condensed:wght@400&family=Open+Sans:wght@400;700&display=swap">
<style>
  :root {
    --page-bg: #e6e6e6;
    --card-white: #f6f6f6;
    --brand-blue: #0198c9;
    --brand-blue-deep: #0389bf;
    --ink: #4a4a4a;
    --ink-soft: #6a6a6a;
    --white: #ffffff;
  }
  html, body {
    margin: 0;
    padding: 0;
    width: 1200px;
    height: 1200px;
    overflow: hidden;
    background: var(--page-bg);
  }
  .canvas {
    position: relative;
    width: 1200px;
    height: 1200px;
  }
  .card {
    position: absolute;
    left: 262px;
    width: 686px;
    height: 392px;
    border-radius: 19px;
    box-sizing: border-box;
  }
  .card--front {
    top: 165px;
    background: var(--card-white);
  }
  .card--back {
    top: 653px;
    background: linear-gradient(180deg, var(--brand-blue) 0%, var(--brand-blue-deep) 100%);
  }
  .holder {
    position: absolute;
    left: 57px;
    top: 84px;
  }
  .holder__name {
    margin: 0;
    font-family: "Roboto", sans-serif;
    font-weight: 700;
    font-size: 23px;
    line-height: 26px;
    color: var(--brand-blue);
  }
  .holder__title {
    margin: 0;
    font-family: "Roboto Condensed", sans-serif;
    font-size: 15px;
    line-height: 20px;
    color: var(--ink-soft);
  }
  .address {
    position: absolute;
    left: 55px;
    top: 176px;
    margin: 0;
    font-family: "Roboto", sans-serif;
    font-size: 15.5px;
    line-height: 19px;
    font-style: normal;
    color: var(--ink);
  }
  .contacts {
    position: absolute;
    left: 58px;
    top: 227px;
    margin: 0;
    padding: 0;
    list-style: none;
    font-family: "Roboto", sans-serif;
    font-size: 15.5px;
    line-height: 19.5px;
    color: var(--ink);
  }
  .contacts li {
    display: flex;
    align-items: center;
    gap: 10px;
  }
  .contacts svg {
    width: 14px;
    height: 14px;
    fill: var(--brand-blue);
    flex: none;
  }
  .brand {
    position: absolute;
    left: 0;
    right: 0;
    top: 0;
    bottom: 0;
    display: flex;
    align-items: center;
    justify-content: center;
    gap: 22px;
  }
  .brand__square {
    width: 86px;
    height: 86px;
    background: var(--white);
    border-radius: 6px;
  }
  .brand__text {
    display: flex;
    flex-direction: column;
    color: var(--white);
    font-family: "Open Sans", sans-serif;
  }
  .brand__name {
    font-weight: 700;
    font-size: 54px;
    line-height: 58px;
    letter-spacing: 0.5px;
  }
  .brand__tagline {
    font-weight: 400;
    font-size: 31px;
    line-height: 34px;
  }
</style>
</head>
<body>
<main class="canvas">

  <section class="card card--front" aria-label="Business card front">
    <div class="holder">
      <h1 class="holder__name">Daniel Morrow</h1>
      <p class="holder__title">Founder &amp; CEO</p>
    </div>
    <address class="address">2140 Linden Court<br>Fairbanks, Alaska 34512</address>
    <ul class="contacts">
      <li>
        <svg viewBox="0 0 24 24" aria-hidden="true"><path d="M6.6 10.8a15.1 15.1 0 0 0 6.6 6.6l2.2-2.2c.3-.3.7-.4 1-.2 1.1.4 2.3.6 3.6.6.6 0 1 .4 1 1V20c0 .6-.4 1-1 1A17 17 0 0 1 3 4c0-.6.4-1 1-1h3.5c.6 0 1 .4 1 1 0 1.3.2 2.5.6 3.6.1.3 0 .7-.2 1z"/></svg>
        555-214-3308
      </li>
      <li>
        <svg viewBox="0 0 24 24" aria-hidden="true"><path d="M7 1h10a2 2 0 0 1 2 2v18a2 2 0 0 1-2 2H7a2 2 0 0 1-2-2V3a2 2 0 0 1 2-2zm0 3v14h10V4zm5 15.5a1 1 0 1 0 0 2 1 1 0 0 0 0-2z"/></svg>
        555-216-7412
      </li>
      <li>
        <svg viewBox="0 0 24 24" aria-hidden="true"><path d="M6 2h12v5H6zM3 9h18a1 1 0 0 1 1 1v8H2v-8a1 1 0 0 1 1-1zm3 5v2h12v-2zM2 19h20v2H2z"/></svg>
        555-219-0625
      </li>
      <li>
        <svg viewBox="0 0 24 24" aria-hidden="true"><path d="M2 5h20v14H2zm2 2v.4l8 5.2 8-5.2V7zm0 2.8V17h16V9.8l-8 5.2z"/></svg>
        hello@clinicsite.com
      </li>
      <li>
        <svg viewBox="0 0 24 24" aria-hidden="true"><path d="M12 2a10 10 0 1 0 0 20 10 10 0 0 0 0-20zm-1 17.9A8 8 0 0 1 4.2 10L9 14.8V16a2 2 0 0 0 2 2zm6.9-2.5A2 2 0 0 0 16 16h-1v-3a1 1 0 0 0-1-1H8v-2h2a1 1 0 0 0 1-1V7h2a2 2 0 0 0 2-2v-.4a8 8 0 0 1 2.9 12.8z"/></svg>
        www.clinicsite.com
      </li>
    </ul>
  </section>

  <section class="card card--back" aria-label="Business card back">
    <div class="brand">
      <div class="brand__square" aria-hidden="true"></div>
      <div class="brand__text">
        <span class="brand__name">SpineWell</span>
        <span class="brand__tagline">INJURY CARE CLINIC</span>
      </div>
    </div>
  </section>

</main>
</body>
</html>
```